PowerPoint Design Project

Hello Dan,nice to talk with you again.
I need a powerpoint template for few aplications:
1st .Vardolux Consult presentation;
2nd.A template to do my jobs and present my reports and presentations to my customers.

I'd like to use the logo you create for me and use the colour we use on the logo as well.

I need also a A4 page to do my offers and reports also using just the logo you did.

Target Market(s)

I work on Business To Business market mainly with industrial customers.

Requirements
Must have
• Same colours as my logo.

```html
<!DOCTYPE html>
<html lang="en">
<head>
<meta charset="UTF-8">
<title>Vardolux Consult – Project Title Slide</title>
<link rel="stylesheet" href="https://fonts.googleapis.com/css2?family=Play&family=Open+Sans:wght@400&display=swap">
<style>
  :root {
    --brand-magenta: #e21e7f;
    --brand-navy: #1d1f6b;
    --ink: #333333;
    --muted: #9a9a9a;
    --rule: #d0d0d0;
    --paper: #ffffff;
  }
  * { margin: 0; padding: 0; box-sizing: border-box; }
  html, body { width: 1200px; height: 900px; overflow: hidden; background: var(--paper); }
  .slide {
    position: relative;
    width: 1200px;
    height: 900px;
    background: var(--paper);
    font-family: "Open Sans", sans-serif;
    color: var(--ink);
  }
  .brand {
    position: absolute;
    left: 45px;
    top: 290px;
    display: flex;
    align-items: center;
    gap: 16px;
  }
  .brand-dot {
    width: 34px;
    height: 34px;
    border-radius: 50%;
    background: var(--brand-magenta);
  }
  .brand-name {
    font-family: "Play", sans-serif;
    font-size: 44px;
    color: var(--brand-magenta);
    letter-spacing: 1px;
  }
  .brand-rule {
    position: absolute;
    left: 45px;
    top: 367px;
    width: 315px;
    height: 2px;
    background: var(--brand-magenta);
    opacity: 0.55;
  }
  .divider-glow {
    position: absolute;
    left: 0;
    top: 402px;
    width: 510px;
    height: 10px;
    background: linear-gradient(to right, rgba(0,0,0,0.07), rgba(0,0,0,0.04) 60%, rgba(0,0,0,0));
    border-radius: 0 6px 6px 0;
  }
  .project-title {
    position: absolute;
    left: 42px;
    top: 428px;
    font-family: "Play", sans-serif;
    font-size: 41px;
    font-weight: 400;
    color: var(--ink);
    letter-spacing: 0.5px;
  }
  .project-title .accent { color: var(--brand-magenta); }
  .project-subtext {
    position: absolute;
    left: 40px;
    top: 494px;
    width: 560px;
    font-size: 21px;
    line-height: 32px;
    color: var(--ink);
  }
  .footer {
    position: absolute;
    left: 0;
    bottom: 0;
    width: 1200px;
    height: 52px;
    border-top: 2px solid var(--rule);
    background: linear-gradient(to bottom, #ffffff, #f1f1f1);
    display: flex;
    justify-content: space-between;
    align-items: center;
    padding: 0 22px;
    font-family: "Play", sans-serif;
    font-size: 22px;
    color: var(--muted);
  }
</style>
</head>
<body>
  <main class="slide">
    <div class="brand">
      <span class="brand-dot"></span>
      <span class="brand-name">Vardolux Consult</span>
    </div>
    <div class="brand-rule"></div>
    <div class="divider-glow"></div>

    <h1 class="project-title"><span class="accent">PROJECT</span> TITLE HERE</h1>
    <p class="project-subtext">Sub text here Sub text here Sub text here Sub text here Sub text here Sub text here Sub text here Sub</p>

    <footer class="footer">
      <span class="page-number">Page No. 00</span>
      <span class="copyright">Copyright@2013</span>
    </footer>
  </main>
</body>
</html>
```